Marlowick community hall home page

We are building a modern, responsive website & booking system for our community hall. For this PixelForge task, we would like to receive design ideas for the home page.
There are no limits on the colours or fonts that can be used. We are looking for a modern, fresh design with a local/community feel. We don’t have a logo but we also recognise that our name is quite long! … So initials (MCH) instead of the name would be fine.
People book our community hall for a range of activities including: fitness classes, wedding receptions, birthday parties, business meetings, teaching, community events, charity fundraisers and other celebrations.
We have three main goals for the website. The first is that people can check our calendar and make a booking for an available time slot. The second is that they can read about our facilities and the prices for hiring them. The third is that people can find out about upcoming activities & events.
CTA: Book now
A button that links to a booking request form. (The form is not part of this design project)
Primary/Header navigation:
Home | Calendar | Facilities | Prices | Photos | News | Contact
Secondary/Footer navigation:
Chatterleaf | Quillcast
Login | Register | Privacy policy | Terms & conditions
Example texts (lorem ipsum etc. is also fine):
We have everything you need from a venue, whether it’s an elegant room with ample flexible space, a lavish and elegant hall for a wedding reception, a conference room that fits 125 delegates or a easy access venue to the town centre.
The hall is available for hire for wedding receptions, birthday celebrations, anniversaries, children's parties, presentations, lectures, fitness groups, and will comfortably accommodate all your guests.
This venue is well equipped with a modern kitchen, a range of audio and technical services, hearing loop, licensed bar, conference facilities, disabled access and unlimited free WiFi.
You can use this website to find out more about our rooms, equipment and the services we can offer and use the calendar to see where we have rooms available. You can also book rooms using our online booking system.
To the front of the building is a large public open grassed area across which is a row of shops. To the rear of the building is the large car park, including spaces for blue badge holders and a large enclosed cycle rack. This area also has extensive gardens, with seating and planting areas maintained by local volunteers.
The community hall is run and managed by volunteers of the Marlowick Community Organisation. Our objectives are to increase opportunities for people living in and around Pepperton.
We are passionate about being the heart of the community; caring for this community centred property and visitors are at the heart of all we do.
Where to go next
— Check when the hall is free
— Read our booking policy documents
— Make a booking reservation
Amenities
— Free WiFi
— Free car parking
— Fully equipped kitchen
— Hearing loop
Details for our most popular facilities (rooms):
Name: Main hall
Short description: A 127 square metre main hall with entrance lobby, toilets, a well-equipped kitchen and separate storage facilities. Three sets of double doors provide access to a large paved area and the adjacent playing field.
Capacity: 180 people
Price: £10-20 per hour
Links: More info | Book now
Name: Large meeting room
Short description: A delightful, spacious room with an outlook and access to the small walled garden. Ideal for meetings and small gatherings - it has its own access door and the use of a disabled W/C. We offer a reduced rate for this room when booked together with the main hall.
Capacity: 20 people
Price: £6-12 per hour
Attachments:
We have attached some photos of the hall & some (royalty free) stock images for inspiration.

```html
<!DOCTYPE html>
<html lang="en">
<head>
<meta charset="utf-8">
<title>Marlowick Community Hall</title>
<link rel="stylesheet" href="https://fonts.googleapis.com/css2?family=Playfair+Display:wght@400;700&family=Open+Sans:wght@400;600;800&display=swap">
<style>
:root{
  --red:#b3121b;
  --red-dark:#8f0d14;
  --ink:#2b2b2b;
  --dark:#2a2522;
  --darker:#141414;
  --grey:#f2f2f2;
  --cell:#e7e7e7;
  --white:#fff;
  --serif:'Playfair Display', Georgia, serif;
  --sans:'Open Sans', Arial, sans-serif;
}
*{box-sizing:border-box;margin:0;padding:0}
html,body{width:1200px;height:5177px;overflow:hidden}
body{font-family:var(--sans);color:var(--ink);background:var(--white);position:relative}
section,header,footer{position:absolute;left:0;width:1200px}
.btn{display:inline-flex;align-items:center;justify-content:center;font-family:var(--serif);color:#fff;background:var(--red);font-size:15px;height:38px;padding:0 16px;text-transform:uppercase;text-decoration:none}
.btn-dark{background:#2b2b2b}
.center{text-align:center}

/* hero */
.hero{top:0;height:710px;background:linear-gradient(180deg,#1c1512 0%,#4a3a2e 45%,#6b5645 75%,#3a2c22 100%)}
.hero-bg{position:absolute;inset:0}
.nav{position:absolute;top:20px;left:144px;right:144px;height:48px;display:flex;align-items:center}
.logo{font-family:var(--serif);font-size:46px;color:#fff;letter-spacing:1px}
.nav ul{list-style:none;display:flex;gap:32px;margin-left:auto;margin-right:34px}
.nav a{font-family:var(--serif);color:#fff;font-size:13px;text-decoration:none}
.nav .current{text-decoration:underline}
.nav .book{border:1px solid #fff;padding:9px 18px;font-family:var(--serif);font-size:13px;color:#fff;text-decoration:none}
.hero h1{position:absolute;top:250px;width:100%;text-align:center;font-family:var(--serif);font-weight:700;font-size:66px;color:#fff}
.hero .check{position:absolute;top:352px;left:452px;width:292px;height:58px;background:rgba(30,30,30,.85);color:#fff;font-family:var(--serif);font-weight:700;font-size:22px;display:flex;align-items:center;justify-content:center}
.arrow{position:absolute;top:322px}
.hero-curve{position:absolute;left:0;bottom:0}

/* welcome */
.welcome{top:710px;height:410px}
.welcome h2{margin-top:72px;font-family:var(--serif);color:var(--red);font-size:32px;font-weight:700}
.welcome p{width:920px;margin:14px auto 0;font-size:15px;line-height:28px;color:#333}
.welcome p+p{margin-top:28px}
.welcome .btn{margin-top:20px}

/* amenities */
.amenities{top:1120px;height:400px;background:#2d2623;overflow:hidden}
.amenities .photo{position:absolute;inset:0;background:linear-gradient(135deg,#4a3f52 0%,#6d5a6e 30%,#8a7b86 55%,#3b2f2a 100%);clip-path:polygon(600px 0,1200px 0,1200px 400px,500px 400px)}
.amenities .wedge{position:absolute;inset:0;background:var(--red);clip-path:polygon(462px 0,600px 0,536px 150px)}
.amenity-list{position:absolute;left:144px;top:78px;list-style:none}
.amenity-list li{display:flex;align-items:center;height:64px;font-family:var(--serif);font-weight:700;font-size:22px;color:#fff;text-transform:uppercase}
.amenity-list svg{width:28px;margin-right:18px}

/* calendar + events */
.schedule{top:1520px;height:718px}
.calendar{position:absolute;left:144px;top:82px;width:432px}
.cal-head{height:42px;background:var(--red);display:flex;align-items:center;justify-content:space-between;padding:0 16px;color:#fff;font-family:var(--serif);font-size:22px}
.cal-days{display:grid;grid-template-columns:repeat(7,1fr);background:#2b2b2b;height:44px;align-items:center;text-align:center;color:#fff;font-size:12px;font-weight:600}
.cal-grid{display:grid;grid-template-columns:repeat(7,1fr);grid-auto-rows:61px;gap:2px;background:#fff;padding-top:2px}
.cal-grid span{background:var(--cell);display:flex;align-items:center;justify-content:center;font-size:19px;color:#333}
.cal-grid .muted{color:#999}
.cal-grid .hot{color:var(--red)}
.events{position:absolute;left:620px;top:72px;width:436px}
.events h3{font-family:var(--serif);font-weight:700;font-size:30px;color:var(--red)}
.event-card{margin-top:12px;height:168px;background:var(--grey);display:flex;padding:10px 12px}
.event-img{width:160px;height:148px;flex:none}
.event-body{padding:14px 0 0 20px}
.event-body h4{font-size:15px;font-weight:600;color:#222}
.event-date{font-size:10px;margin-top:6px}
.event-body p{font-size:9.5px;line-height:17px;color:#777;margin-top:8px}
.event-body a{display:block;font-size:10px;color:var(--red);margin-top:8px}
.events h3.second{margin-top:38px}
.schedule .btn{position:absolute;left:540px;top:582px;width:120px}

/* facilities */
.facilities{top:2238px;height:807px;background:radial-gradient(ellipse at 50% 40%,#3d3632 0%,#2a2421 70%,#1f1a18 100%)}
.facilities h2{margin-top:66px;font-family:var(--serif);font-weight:400;font-size:60px;color:#fff}
.room{position:absolute;top:172px;width:434px;height:538px;background:#fff;text-align:center;padding:0 26px}
.room-img{width:136px;height:136px;border-radius:50%;margin:28px auto 0}
.room h3{margin-top:22px;font-family:var(--serif);font-weight:700;font-size:30px;color:var(--red);text-transform:uppercase}
.room p{margin-top:14px;font-size:12px;line-height:24px;color:#444}
.room .stat{font-weight:800;font-size:22px;color:#111;text-transform:uppercase;line-height:40px}
.room .stat:first-of-type{margin-top:20px}
.room-actions{margin-top:16px;display:flex;justify-content:center;gap:12px}
.room-actions .btn{height:36px;font-size:14px}

/* activities */
.activities{top:3045px;height:615px}
.activities h2{margin-top:78px;font-family:var(--serif);font-weight:700;font-size:32px;line-height:48px;color:var(--red)}
.act-grid{position:absolute;left:144px;top:190px;width:912px;display:grid;grid-template-columns:repeat(4,218px);grid-auto-rows:160px;gap:16px 13px}
.act{border:1px solid #c9c9c9;box-shadow:0 1px 4px rgba(0,0,0,.12);display:flex;flex-direction:column;align-items:center;justify-content:center}
.act svg{width:60px;height:60px;stroke:var(--red);fill:none;stroke-width:2.2;stroke-linecap:round;stroke-linejoin:round}
.act span{margin-top:16px;font-size:14px;font-weight:600;color:#333}

/* photos */
.photos{top:3660px;height:760px;background:radial-gradient(ellipse at 50% 40%,#3d3632 0%,#2a2421 70%,#1f1a18 100%)}
.photos h2{margin-top:70px;font-family:var(--serif);font-weight:400;font-size:60px;color:#fff}
.ph{position:absolute}
.photos .btn{position:absolute;top:640px;left:540px;width:120px}

/* location */
.location{top:4420px;height:540px}
.location h2{margin-top:84px;font-family:var(--serif);font-weight:700;font-size:62px;color:var(--red)}
.map{position:absolute;left:144px;top:180px;width:912px;height:360px;background:linear-gradient(135deg,#e9ecef 0%,#dfe5e0 40%,#cfe3ea 60%,#e8ebee 100%)}
.map svg{position:absolute;left:512px;top:60px}

/* footer */
.footer{top:4960px;height:217px;background:var(--darker);text-align:center}
.contact-bar{width:912px;height:44px;margin:0 auto;background:var(--red);color:#fff;font-size:14px;display:flex;align-items:center;justify-content:center;gap:14px}
.contact-bar svg{vertical-align:-2px;margin-right:6px}
.foot-links{margin-top:36px;font-size:11px;color:#ccc}
.copy{margin-top:16px;font-size:11px;color:#ccc}
.social{margin-top:22px;display:flex;justify-content:center;gap:26px;font-size:12px;color:#ddd;align-items:center}
.social span{display:inline-flex;align-items:center;gap:8px}
.social i{width:14px;height:14px;border:1px solid #aaa;border-radius:50%;display:inline-block}
</style>
</head>
<body>

<header class="hero">
  <div class="hero-bg" role="img" aria-label="Photo of the main hall set for a wedding reception with round tables and a chandelier"></div>
  <nav class="nav">
    <div class="logo">MCH</div>
    <ul>
      <li><a class="current" href="#">Home</a></li>
      <li><a href="#">Calendar</a></li>
      <li><a href="#">Facilities</a></li>
      <li><a href="#">Prices</a></li>
      <li><a href="#">Photos</a></li>
      <li><a href="#">News</a></li>
      <li><a href="#">Contact</a></li>
    </ul>
    <a class="book" href="#">Book Now</a>
  </nav>
  <h1>Marlowick Community Hall</h1>
  <div class="check">CHECK AVAILABILITY</div>
  <svg class="arrow" style="left:62px" width="24" height="36" viewBox="0 0 24 36"><path d="M18 4 6 18l12 14" stroke="#fff" stroke-width="4" fill="none"/></svg>
  <svg class="arrow" style="left:1114px" width="24" height="36" viewBox="0 0 24 36"><path d="M6 4l12 14L6 32" stroke="#fff" stroke-width="4" fill="none"/></svg>
  <svg class="hero-curve" width="1200" height="110" viewBox="0 0 1200 110">
    <path d="M0 12 Q600 150 1200 12 L1200 110 L0 110Z" fill="var(--red)"/>
    <path d="M0 24 Q600 170 1200 4 L1200 110 L0 110Z" fill="#fff"/>
  </svg>
</header>

<section class="welcome center">
  <h2>Welcome to MCH</h2>
  <p>We have everything you need from a venue, whether it’s an elegant room with ample flexible space, a lavish and elegant hall for a wedding reception, a conference room that fits 125 delegates or a easy access venue to the town centre.</p>
  <p>The hall is available for hire for wedding receptions, birthday celebrations, anniversaries, children's parties, presentations, lectures, fitness groups, and will comfortably accommodate all your guests.</p>
  <a class="btn" href="#">Read more</a>
</section>

<section class="amenities">
  <div class="photo" role="img" aria-label="Photo of guests at round tables in the hall with stained glass windows"></div>
  <div class="wedge"></div>
  <ul class="amenity-list">
    <li><svg viewBox="0 0 28 22" fill="none" stroke="#fff" stroke-width="3" stroke-linecap="round"><path d="M2 8a17 17 0 0 1 24 0M6 12a11 11 0 0 1 16 0M10 16a5 5 0 0 1 8 0"/><circle cx="14" cy="19" r="1.5" fill="#fff"/></svg>Free WiFi</li>
    <li><svg viewBox="0 0 28 20" fill="#fff"><path d="M5 8l3-6h12l3 6h3v8h-3v3h-4v-3H10v3H6v-3H2V8z"/><circle cx="7" cy="12" r="2" fill="#2d2623"/><circle cx="21" cy="12" r="2" fill="#2d2623"/></svg>Free car parking</li>
    <li><svg viewBox="0 0 24 26" fill="#fff"><path d="M3 1h2v8h2V1h2v8h2V1h2v10a4 4 0 0 1-3 3v11H7V14a4 4 0 0 1-4-3zM18 1c3 0 4 4 4 9h-2v15h-3V1z"/></svg>Fully equipped kitchen</li>
    <li><svg viewBox="0 0 28 22" fill="#fff"><path d="M2 7h5l7-6v20l-7-6H2z"/><path d="M18 6a6 6 0 0 1 0 10M21 2a11 11 0 0 1 0 18" stroke="#fff" stroke-width="2.5" fill="none"/></svg>Hearing loop</li>
  </ul>
</section>

<section class="schedule">
  <div class="calendar">
    <div class="cal-head">
      <svg width="22" height="22" viewBox="0 0 22 22"><circle cx="11" cy="11" r="11" fill="#fff"/><path d="M13 6l-5 5 5 5" stroke="var(--red)" stroke-width="2.5" fill="none"/></svg>
      <span>FEBRUARY 2021</span>
      <svg width="22" height="22" viewBox="0 0 22 22"><circle cx="11" cy="11" r="11" fill="#fff"/><path d="M9 6l5 5-5 5" stroke="var(--red)" stroke-width="2.5" fill="none"/></svg>
    </div>
    <div class="cal-days"><span>Mon</span><span>Tue</span><span>Wed</span><span>Thu</span><span>Fri</span><span>Sat</span><span>Sun</span></div>
    <div class="cal-grid">
      <span class="muted">28</span><span class="muted">29</span><span class="muted">30</span><span class="muted">31</span><span>1</span><span class="hot">2</span><span>3</span>
      <span>4</span><span class="hot">5</span><span>6</span><span>7</span><span>8</span><span>9</span><span>10</span>
      <span>11</span><span>12</span><span>13</span><span>14</span><span>15</span><span class="hot">16</span><span>17</span>
      <span>18</span><span>19</span><span>20</span><span class="hot">21</span><span>22</span><span>23</span><span>24</span>
      <span>25</span><span>26</span><span class="hot">27</span><span>28</span><span>29</span><span>30</span><span>31</span>
      <span class="muted">1</span><span class="muted">2</span><span class="muted">3</span><span class="muted">4</span><span class="muted">5</span><span class="muted">6</span><span class="muted">7</span>
    </div>
  </div>

  <div class="events">
    <h3>Upcoming Events</h3>
    <div class="event-card">
      <div class="event-img" role="img" aria-label="Photo of a decorated wedding table with candles" style="background:linear-gradient(135deg,#3a3028,#8a7560 50%,#d9d2c6)"></div>
      <div class="event-body">
        <h4>Fusce eget neque</h4>
        <div class="event-date">6 February, 2021</div>
        <p>Sed augue orci, elementum in magna congue, tincidunt vulputate erat. Aliquam consectetur orci molestie dictum molestie.</p>
        <a href="#">VIEW ALL</a>
      </div>
    </div>
    <h3 class="second">Upcoming Activities</h3>
    <div class="event-card">
      <div class="event-img" role="img" aria-label="Photo of a yoga class in a bright room" style="background:linear-gradient(135deg,#e9e4de,#c9bfb4 50%,#8c8276)"></div>
      <div class="event-body">
        <h4>Fusce eget neque</h4>
        <div class="event-date">6 February, 2021</div>
        <p>Sed augue orci, elementum in magna congue, tincidunt vulputate erat. Aliquam consectetur orci molestie dictum molestie.</p>
        <a href="#">VIEW ALL</a>
      </div>
    </div>
  </div>
  <a class="btn" href="#">Book now</a>
</section>

<section class="facilities center">
  <h2>Our Facilities and The Prices</h2>
  <article class="room" style="left:144px">
    <div class="room-img" role="img" aria-label="Photo of the main hall with dining tables" style="background:linear-gradient(160deg,#c9a96a,#3c4a6c 60%,#e8e6e4)"></div>
    <h3>Main Hall</h3>
    <p>A 127 square metre main hall with entrance lobby, toilets, a well-equipped kitchen and separate storage facilities. Three sets of double doors provide access to a large paved area and the adjacent playing field.</p>
    <div class="stat">Capacity: 180 people</div>
    <div class="stat">Price: £10-20 per hour</div>
    <div class="room-actions"><a class="btn btn-dark" href="#">More info</a><a class="btn" href="#">Book now</a></div>
  </article>
  <article class="room" style="left:622px">
    <div class="room-img" role="img" aria-label="Photo of the large meeting room with a long table" style="background:linear-gradient(160deg,#9aa0a3,#5a4a3c 55%,#2f2a26)"></div>
    <h3>Large Meeting Room</h3>
    <p>A delightful, spacious room with an outlook and access to the small walled garden. Ideal for meetings and small gatherings - it has its own access door and the use of a disabled W/C. We offer a reduced rate for this room when booked together with the main hall.</p>
    <div class="stat">Capacity: 20 people</div>
    <div class="stat">Price: £6-12 per hour</div>
    <div class="room-actions"><a class="btn btn-dark" href="#">More info</a><a class="btn" href="#">Book now</a></div>
  </article>
</section>

<section class="activities center">
  <h2>People book our community hall for a<br>range of activities including :</h2>
  <div class="act-grid">
    <div class="act"><svg viewBox="0 0 60 60"><path d="M8 30h44M12 22v16M18 18v24M42 18v24M48 22v16"/></svg><span>Fitness Classes</span></div>
    <div class="act"><svg viewBox="0 0 60 60"><path d="M12 54V28a18 18 0 0 1 36 0v26M8 54h44M30 10V4M24 20h12"/></svg><span>Wedding Receptions</span></div>
    <div class="act"><svg viewBox="0 0 60 60"><path d="M10 54h40V40H10zM14 40V30h32v10M22 30v-8M30 30v-8M38 30v-8M22 18v-2M30 18v-2M38 18v-2M10 46q5 4 10 0t10 0 10 0 10 0"/></svg><span>Birthday Parties</span></div>
    <div class="act"><svg viewBox="0 0 60 60"><path d="M8 20h44v30H8zM22 20v-6h16v6M8 32h44M28 30h4v4h-4z"/></svg><span>Business Meetings</span></div>
    <div class="act"><svg viewBox="0 0 60 60"><path d="M10 8h40v28H10zM18 18h14M18 26h22M24 36l-6 16M36 36l6 16M30 36v8"/></svg><span>Teaching</span></div>
    <div class="act"><svg viewBox="0 0 60 60"><circle cx="16" cy="22" r="6"/><circle cx="30" cy="18" r="7"/><circle cx="44" cy="22" r="6"/><path d="M6 50v-8a10 10 0 0 1 20 0M19 50v-9a11 11 0 0 1 22 0v9M34 50v-8a10 10 0 0 1 20 0"/></svg><span>Community Events</span></div>
    <div class="act"><svg viewBox="0 0 60 60"><path d="M30 48 12 30a10 10 0 0 1 18-12 10 10 0 0 1 18 12z"/><path d="M6 54h48"/></svg><span>Charity Fundraisers</span></div>
    <div class="act"><svg viewBox="0 0 60 60"><ellipse cx="20" cy="18" rx="9" ry="11"/><ellipse cx="40" cy="18" rx="9" ry="11"/><path d="M20 29q4 10-2 25M40 29q-4 10 2 25"/></svg><span>Other Celebrations</span></div>
  </div>
</section>

<section class="photos center">
  <h2>Photos</h2>
  <div class="ph" role="img" aria-label="Photo of the red brick hall building against a blue sky" style="left:144px;top:166px;width:448px;height:446px;background:linear-gradient(180deg,#2f5fa8 0%,#8fb3dc 35%,#9a4a2e 60%,#6a2e1c 85%,#3f6a2a 100%)"></div>
  <div class="ph" role="img" aria-label="Photo of children on a bouncy castle" style="left:606px;top:166px;width:218px;height:214px;background:linear-gradient(180deg,#9ec3e8,#e8d24a 55%,#c9a520)"></div>
  <div class="ph" role="img" aria-label="Photo of stained glass windows above a dining hall" style="left:838px;top:166px;width:218px;height:214px;background:linear-gradient(180deg,#c2551f,#2f6aa8 45%,#e4e4ea 80%,#2a3f7a)"></div>
  <div class="ph" role="img" aria-label="Photo of a conference room with a long table and screen" style="left:606px;top:398px;width:218px;height:214px;background:linear-gradient(180deg,#e8e8ea,#c9c6c2 50%,#3a3a40)"></div>
  <div class="ph" role="img" aria-label="Photo of a blue yoga mat being rolled out" style="left:838px;top:398px;width:218px;height:214px;background:linear-gradient(180deg,#f1efe9,#d8b8a2 40%,#1f5fa8 70%,#174a86)"></div>
  <a class="btn" href="#">View all</a>
</section>

<section class="location center">
  <h2>Location</h2>
  <div class="map" role="img" aria-label="Street map showing the hall location">
    <svg width="44" height="60" viewBox="0 0 44 60"><path d="M22 58C8 38 2 30 2 21a20 20 0 0 1 40 0c0 9-6 17-20 37z" fill="var(--red)"/><circle cx="22" cy="21" r="8" fill="#fff"/></svg>
  </div>
</section>

<footer class="footer">
  <div class="contact-bar">
    <span><svg width="12" height="16" viewBox="0 0 12 16"><path d="M6 16C1 9 0 7 0 5.5a6 6 0 0 1 12 0C12 7 11 9 6 16z" fill="#fff"/><circle cx="6" cy="6" r="2.2" fill="var(--red)"/></svg>12 Orchard Row, Marlowick, MK4 7HL</span>
    <span>|</span>
    <span><svg width="14" height="14" viewBox="0 0 14 14"><path d="M3 0l3 3-2 2a8 8 0 0 0 5 5l2-2 3 3-2 3C5 14 0 9 0 3z" fill="#fff"/></svg>Phone : 0161 555 0142</span>
    <span>|</span>
    <span><svg width="16" height="12" viewBox="0 0 16 12"><rect width="16" height="12" fill="#fff"/><path d="M0 0l8 7 8-7" stroke="var(--red)" stroke-width="1.5" fill="none"/></svg>Email : info@marlowickhall.org</span>
  </div>
  <div class="foot-links">Home | Calendar | Facilities | Prices | Photos | News | Contact &nbsp;| Login | Register | Privacy policy | Terms &amp; conditions</div>
  <div class="copy">Copyright © 2021 &nbsp;Marlowick Community Hall. &nbsp;All rights reserved.</div>
  <div class="social"><span><i></i>Chatterleaf</span><span><i></i>Quillcast</span></div>
</footer>

</body>
</html>
```